Letterbox flyer design

Hi - hoping you're able to help design a flyer for letterbox delivery. I think it needs to be 99mm x 210mm.

Side 1 - Large Logo, dark back ground.
Larger text - "5%* Property Management."
Medium Text - "Better Services, Lower Fee's, Higher Yields"
Smaller text at bottom - "0472 519 084 - gideon@pellbrook.com.au - pellbrook.com.au"

Back Side -
• Management Fee – 5%+GST of rent collected (no rent paid = no mgmt. fee charged)
• An Establishment fee of $500 for new tenancies we establish.
• Marketing Costs as Required and agreed to between parties.
• No Fee’s for Condition Reports, inspections, re-listing, tenancy renewal, admin costs, or any other ‘sundry’ charges.
• All rent is paid out monthly, yearly ‘profit-and-loss’ statements at no cost.
• Ingoing condition report is produced prior to occupancy, and routine condition inspections are conducted after the first 3months, then every 6months.
• Open homes are advertised in advance, and held on the weekend and one lunchtime or evening per week.
• All applicants are vetted, with the most suitable sent through for your consideration and approval.
• Advise on different tenancy terms as they could have the ability to affect the long-term yields.

```html
<!DOCTYPE html>
<html lang="en">
<head>
<meta charset="utf-8">
<title>Pellbrook Property Services – Letterbox Flyer</title>
<link rel="stylesheet" href="https://fonts.googleapis.com/css2?family=Bebas+Neue&family=Montserrat:wght@500;700;800&display=swap">
<style>
  :root {
    --teal: #43bec8;
    --slate: #5d595c;
    --ink: #000000;
    --paper: #ffffff;
    --brand-grey: #8a878a;
    --backdrop: #e6e6e6;
  }
  * { margin: 0; padding: 0; box-sizing: border-box; }
  html, body {
    width: 1200px;
    height: 1112px;
    overflow: hidden;
    background: var(--backdrop);
  }
  .flyer {
    position: absolute;
    top: 133px;
    width: 397px;
    height: 841px;
    overflow: hidden;
  }
  .flyer--front { left: 153px; }
  .flyer--back { left: 650px; }
  .flyer__art {
    position: absolute;
    inset: 0;
    width: 397px;
    height: 841px;
    display: block;
  }
  .headline { font-family: "Montserrat", sans-serif; font-weight: 800; }
  .brand-name {
    font-family: "Montserrat", sans-serif;
    font-weight: 700;
    fill: var(--brand-grey);
  }
  .tagline { font-family: "Bebas Neue", sans-serif; fill: var(--paper); }
  .contact { font-family: "Montserrat", sans-serif; font-weight: 500; font-size: 13.5px; fill: var(--paper); }

  .fee-list {
    position: absolute;
    top: 162px;
    left: 30px;
    width: 352px;
    list-style: none;
    font-family: "Montserrat", sans-serif;
    font-weight: 500;
    font-size: 14px;
    line-height: 18.6px;
    color: var(--paper);
  }
  .fee-list__item {
    position: relative;
    margin-bottom: 18.6px;
  }
  .fee-list__item::before {
    content: "";
    position: absolute;
    left: -14px;
    top: 5px;
    width: 6px;
    height: 6px;
    border-radius: 50%;
    border: 1.6px solid transparent;
    border-right-color: var(--teal);
    border-bottom-color: var(--teal);
  }
  .highlight {
    background: var(--teal);
    color: var(--paper);
    padding: 0 1px;
    border-radius: 2px;
  }
</style>
</head>
<body>

<section class="flyer flyer--front" aria-label="Flyer front">
  <svg class="flyer__art" viewBox="0 0 397 841" xmlns="http://www.w3.org/2000/svg">
    <rect class="panel-top" width="397" height="841" fill="var(--slate)"/>
    <path class="panel-dark" d="M0 196 H201 C280 196 331 250 331 324 C331 380 355 418 397 432 V592 H0 Z" fill="var(--ink)"/>
    <rect class="panel-teal" y="592" width="397" height="249" fill="var(--teal)"/>
    <path class="panel-contact" d="M0 765 H207 C265 765 306 795 322 841 H0 Z" fill="var(--ink)"/>

    <text class="headline" x="212" y="93" text-anchor="middle" font-size="72" fill="var(--teal)">5%*</text>
    <text class="headline" x="212" y="144" text-anchor="middle" font-size="50" fill="var(--paper)">PROPERTY</text>
    <text class="headline" x="212" y="179" text-anchor="middle" font-size="36" fill="var(--paper)">MANAGEMENT</text>

    <text class="brand-name" x="190" y="410" text-anchor="middle" font-size="46">PELLBROOK</text>
    <text class="brand-name" x="190" y="446" text-anchor="middle" font-size="23">PROPERTY SERVICES</text>

    <text class="tagline" x="198" y="639" text-anchor="middle" font-size="48">BETTER SERVICES</text>
    <text class="tagline" x="198" y="692" text-anchor="middle" font-size="48">LOWER FEE'S</text>
    <text class="tagline" x="198" y="745" text-anchor="middle" font-size="48">HIGHER YIELDS</text>

    <g class="contact-icons" fill="var(--teal)">
      <path d="M23 780 l3 -1 1.5 3 -1.5 1.2 q1 2.2 3 3.3 l1.2 -1.5 3 1.4 -1 3 q-6 0 -9.2 -9.4z"/>
      <rect x="22" y="802" width="10" height="7" rx="1"/>
      <path d="M22.5 802.5 l4.5 4 4.5 -4" stroke="var(--ink)" stroke-width="1" fill="none"/>
      <circle cx="27" cy="827" r="5.2" fill="none" stroke="var(--teal)" stroke-width="1.3"/>
      <path d="M21.8 827 h10.4 M27 821.8 v10.4" stroke="var(--teal)" stroke-width="1"/>
    </g>
    <text class="contact" x="38" y="789">0472 519 084</text>
    <text class="contact" x="38" y="810">gideon@pellbrook.com.au</text>
    <text class="contact" x="38" y="831">www.pellbrook.com.au</text>
  </svg>
</section>

<section class="flyer flyer--back" aria-label="Flyer back">
  <svg class="flyer__art" viewBox="0 0 397 841" xmlns="http://www.w3.org/2000/svg">
    <rect class="panel-teal" width="397" height="130" fill="var(--teal)"/>
    <path class="panel-dark" d="M78 19 H397 V841 H0 V117 C18 103 21 88 21 72 C21 40 45 19 78 19 Z" fill="var(--ink)"/>
    <path class="panel-contact" d="M0 766 H205 C262 766 305 796 320 841 H0 Z" fill="var(--slate)"/>

    <text class="brand-name" x="48" y="78" font-size="30">PELLBROOK</text>
    <text class="brand-name" x="48" y="100" font-size="15">PROPERTY SERVICES</text>

    <g class="contact-icons" fill="var(--teal)">
      <path d="M23 781 l3 -1 1.5 3 -1.5 1.2 q1 2.2 3 3.3 l1.2 -1.5 3 1.4 -1 3 q-6 0 -9.2 -9.4z"/>
      <rect x="22" y="803" width="10" height="7" rx="1"/>
      <path d="M22.5 803.5 l4.5 4 4.5 -4" stroke="var(--slate)" stroke-width="1" fill="none"/>
      <circle cx="27" cy="828" r="5.2" fill="none" stroke="var(--teal)" stroke-width="1.3"/>
      <path d="M21.8 828 h10.4 M27 822.8 v10.4" stroke="var(--teal)" stroke-width="1"/>
    </g>
    <text class="contact" x="38" y="790">0472 519 084</text>
    <text class="contact" x="38" y="811">gideon@pellbrook.com.au</text>
    <text class="contact" x="38" y="832">www.pellbrook.com.au</text>
  </svg>

  <ul class="fee-list">
    <li class="fee-list__item">Management Fee – <span class="highlight">5%+GST</span> of rent collected (no rent paid = no mgmt. fee charged)</li>
    <li class="fee-list__item">An Establishment fee of <span class="highlight">$500</span> for new tenancies we establish.</li>
    <li class="fee-list__item">Marketing Costs as Required and agreed to between parties.</li>
    <li class="fee-list__item">No Fee’s for Condition Reports, inspections, re-listing, tenancy renewal, admin costs, or any other ‘sundry’ charges.</li>
    <li class="fee-list__item">All rent is paid out monthly, yearly ‘profit-and-loss’ statements at no cost.</li>
    <li class="fee-list__item">Ingoing condition report is produced prior to occupancy, and routine condition inspections are conducted after the first <span class="highlight">3months,</span> then every 6months.</li>
    <li class="fee-list__item">Open homes are advertised in advance, and held on the weekend and one lunchtime or evening per week.</li>
    <li class="fee-list__item">All applicants are vetted, with the most suitable sent through for your consideration and approval.</li>
    <li class="fee-list__item">Advise on different tenancy terms as they could have the ability to affect the long-term yields.</li>
  </ul>
</section>

</body>
</html>
```